Re-Design a Business Card for a Website & App Development Company

Hi there,

I am looking for someone to re-design an existing business card for a website and app development company.

The colors of the company are primarily orange and white.
Attached is the existing business card for inspiration and the company logo.

Looking for a business card that is sleek, modern and easily readable.

```html
<!DOCTYPE html>
<html lang="en">
<head>
<meta charset="utf-8">
<title>Kernel Forge – Business Card</title>
<link href="https://fonts.googleapis.com/css2?family=Lato:wght@400;700;900&display=swap" rel="stylesheet">
<style>
  :root {
    --bg: #3a3a3a;
    --ink: #111111;
    --paper: #ffffff;
    --orange: #f26a1b;
    --muted: #2b2b2b;
  }
  * { box-sizing: border-box; margin: 0; padding: 0; }
  html, body { width: 1200px; height: 821px; overflow: hidden; }
  body {
    background: var(--bg);
    font-family: "Lato", sans-serif;
    position: relative;
  }
  .card {
    position: absolute;
    width: 520px;
    height: 300px;
    border-radius: 16px;
    overflow: hidden;
    box-shadow: 0 10px 30px rgba(0,0,0,0.35);
  }

  /* Back side */
  .card--back {
    left: 80px; top: 110px;
    background: var(--ink);
    color: var(--paper);
  }
  .card--back .brand {
    position: absolute;
    left: 0; right: 0; top: 92px;
    text-align: center;
  }
  .brand-name {
    display: inline-flex;
    align-items: center;
    gap: 10px;
    font-weight: 900;
    font-size: 40px;
    letter-spacing: -0.5px;
    line-height: 1;
  }
  .brand-mark {
    width: 22px; height: 22px;
    background: var(--orange);
    display: inline-block;
  }
  .tagline {
    margin-top: 8px;
    font-weight: 700;
    font-size: 13px;
  }
  .tagline .accent, .site .accent { color: var(--orange); }
  .card--back .site {
    position: absolute;
    left: 0; right: 0; bottom: 26px;
    text-align: center;
    font-size: 12px;
    font-weight: 700;
    color: var(--orange);
  }
  .card--back .site span { color: var(--paper); }

  /* Front side */
  .card--front {
    left: 600px; top: 410px;
    background: var(--paper);
    color: var(--ink);
  }
  .card--front .brand {
    position: absolute;
    left: 34px; top: 100px;
  }
  .card--front .brand-name { color: var(--ink); font-size: 36px; }
  .card--front .tagline { color: var(--ink); font-size: 12px; }
  .divider {
    position: absolute;
    left: 318px; top: 60px;
    width: 1px; height: 120px;
    background: var(--orange);
  }
  .contact {
    position: absolute;
    right: 28px; top: 52px;
    text-align: right;
  }
  .contact .person {
    font-size: 19px;
    font-weight: 700;
    color: var(--orange);
    line-height: 1.1;
  }
  .contact .role {
    font-size: 11px;
    margin-bottom: 14px;
  }
  .contact ul { list-style: none; }
  .contact li {
    display: flex;
    justify-content: flex-end;
    align-items: center;
    gap: 8px;
    font-size: 11.5px;
    line-height: 18px;
  }
  .contact li svg { width: 11px; height: 11px; flex: none; }
  .band {
    position: absolute;
    left: 0; bottom: 0;
    width: 520px; height: 56px;
  }
</style>
</head>
<body>

  <section class="card card--back" aria-label="Card back">
    <div class="brand">
      <div class="brand-name"><i class="brand-mark"></i>Kernel Forge</div>
      <p class="tagline">Website &amp; App <span class="accent">Development</span> Agency</p>
    </div>
    <p class="site">www.<span>KernelForge</span>.co.nz</p>
  </section>

  <section class="card card--front" aria-label="Card front">
    <div class="brand">
      <div class="brand-name"><i class="brand-mark"></i>Kernel Forge</div>
      <p class="tagline">Website &amp; App Development Agency</p>
    </div>

    <div class="divider"></div>

    <div class="contact">
      <p class="person">Mara Tillson</p>
      <p class="role">President &amp; CEO</p>
      <ul>
        <li>555-014-220-00
          <svg viewBox="0 0 24 24" aria-hidden="true"><path fill="#f26a1b" d="M6.6 10.8a15 15 0 0 0 6.6 6.6l2.2-2.2c.3-.3.7-.4 1-.2 1.1.4 2.3.6 3.6.6.6 0 1 .4 1 1V20c0 .6-.4 1-1 1A17 17 0 0 1 3 4c0-.6.4-1 1-1h3.5c.6 0 1 .4 1 1 0 1.3.2 2.5.6 3.6.1.3 0 .7-.2 1z"/></svg>
        </li>
        <li>hello@kernelforge.com
          <svg viewBox="0 0 24 24" aria-hidden="true"><rect x="2" y="5" width="20" height="14" rx="2" fill="#f26a1b"/><path d="M3 6l9 7 9-7" fill="none" stroke="#fff" stroke-width="2"/></svg>
        </li>
        <li>www.kernelforge.com
          <svg viewBox="0 0 24 24" aria-hidden="true"><circle cx="12" cy="12" r="9" fill="none" stroke="#f26a1b" stroke-width="2.4"/><path d="M3 12h18M12 3c3 3 3 15 0 18M12 3c-3 3-3 15 0 18" fill="none" stroke="#f26a1b" stroke-width="1.8"/></svg>
        </li>
      </ul>
    </div>

    <svg class="band" viewBox="0 0 520 56" preserveAspectRatio="none" aria-hidden="true">
      <polygon points="0,40 400,16 390,56 0,56" fill="#f26a1b"/>
      <polygon points="400,16 520,9 520,56 390,56" fill="#111111"/>
    </svg>
  </section>

</body>
</html>
```